Timid Kitten Clinic Business Card Design

I need a business card designed for my cat only veterinary clinic. I will upload the logo that I would like included on the card. Please include:
Business Name: The Timid Kitten Clinic
Address: 4827 W. 39th Ln, Scottsdale, AZ 85317
Phone #: 480-555-6314
Website URL: www.timidkittenvet.example
And the Doctors Name: Marla Quint, DVM

```html
<!DOCTYPE html>
<html lang="en">
<head>
<meta charset="utf-8">
<title>The Timid Kitten Clinic – Business Card</title>
<link rel="stylesheet" href="https://fonts.googleapis.com/css2?family=Comfortaa:wght@500&family=Montserrat:wght@400;700&display=swap">
<style>
  :root {
    --backdrop: #ece8e1;
    --card: #ffffff;
    --card-front: #f7f7f7;
    --green: #3a7d2c;
    --ink: #111111;
    --text-grey: #333333;
    --mark-dark: #1c1630;
  }
  * { margin: 0; padding: 0; box-sizing: border-box; }
  html, body { width: 900px; height: 1200px; overflow: hidden; }
  body { background: var(--backdrop); position: relative; font-family: "Montserrat", sans-serif; }

  .card {
    position: absolute; left: 80px; width: 742px; height: 440px;
    border-radius: 30px; overflow: hidden;
    box-shadow: 0 4px 10px rgba(0,0,0,0.25);
  }
  .card--front { top: 132px; background: var(--card-front); }
  .card--back { top: 638px; background: var(--card); }
  .card__waves { position: absolute; left: 0; top: 0; width: 742px; height: 440px; }

  .brand { position: absolute; display: flex; align-items: center; }
  .brand__mark { border-radius: 50%; background: radial-gradient(circle at 50% 45%, #3a3560, var(--mark-dark)); flex: none; }
  .brand__name { font-family: "Comfortaa", sans-serif; font-weight: 500; color: var(--ink); }

  .card--front .brand { left: 38px; top: 174px; }
  .card--front .brand__mark { width: 112px; height: 112px; }
  .card--front .brand__name { margin-left: 7px; font-size: 24px; line-height: 28px; letter-spacing: 0.5px; }

  .divider { position: absolute; left: 374px; top: 148px; width: 2px; height: 146px; background: var(--green); }

  .contact { position: absolute; left: 409px; top: 143px; color: var(--text-grey); }
  .contact__name { font-weight: 700; font-size: 27px; color: var(--green); line-height: 34px; }
  .contact__address { margin-top: 17px; font-size: 16px; line-height: 20px; }
  .contact__list { list-style: none; margin-top: 15px; font-size: 16px; line-height: 22px; }
  .contact__list li { display: flex; align-items: center; }
  .contact__list svg { width: 13px; height: 13px; margin-right: 14px; fill: var(--green); }

  .card--back .brand { left: 113px; top: 127px; }
  .card--back .brand__mark { width: 190px; height: 190px; }
  .card--back .brand__name { margin-left: 15px; font-size: 44px; line-height: 46px; letter-spacing: 1.5px; }

  .card__band { position: absolute; left: 0; bottom: 0; width: 100%; height: 13px; background: var(--green); }
</style>
</head>
<body>

<section class="card card--front">
  <svg class="card__waves" viewBox="0 0 742 440" aria-hidden="true">
    <path d="M0 352 C70 378 180 400 270 408 C170 412 70 400 0 384 Z" fill="var(--ink)"/>
    <path d="M0 404 C200 400 470 372 742 392 L742 440 L0 440 Z" fill="var(--green)"/>
  </svg>

  <div class="brand">
    <div class="brand__mark" role="img" aria-label="Clinic emblem circle"></div>
    <p class="brand__name">The Timid<br>Kitten Clinic</p>
  </div>

  <div class="divider"></div>

  <div class="contact">
    <h1 class="contact__name">Marla Quint, DVM</h1>
    <p class="contact__address">4827 W. 39th Ln, Scottsdale<br>AZ 85317</p>
    <ul class="contact__list">
      <li><svg viewBox="0 0 16 16" aria-hidden="true"><path d="M1 5 C1 2 15 2 15 5 L15 7 L11 7 L11 5 L5 5 L5 7 L1 7 Z M3 8 L13 8 L14 15 L2 15 Z"/></svg>480-555-6314</li>
      <li><svg viewBox="0 0 16 16" aria-hidden="true"><circle cx="8" cy="8" r="7"/></svg>www.timidkittenvet.example</li>
    </ul>
  </div>
</section>

<section class="card card--back">
  <div class="brand">
    <div class="brand__mark" role="img" aria-label="Clinic emblem circle"></div>
    <p class="brand__name">The Timid<br>Kitten Clinic</p>
  </div>
  <div class="card__band"></div>
</section>

</body>
</html>
```